Design an exclusive flyer for a ski school that focuses on private lessons
Needs
Design a modern and engaging flyer for higher income customers. The flyer is intended to attract attention. The flyers are on the shelves at the ski pass counter. Since most flyers are very colorful with plenty of pictures, we would like to use clearer lines and less or no picture material. The ski school is in Sölden (Tyrol, Austria).
The dimensions should be that of a postcard (10.5cm x 14.8cm)
Front: - Logo (here you can also choose the colors freely)
- Private lessons
- learn differently
-Sölden
Back: should read the following in German and English ...
Private lessons (the better you drive, the more fun you have)
Private Lessons (the better you ride the more you enjoy)
For families & friends (finally going on vacation together)
Families & Friends (go on holidays together)
Freeride & ski tours (an unforgettable mountain experience)
Freeride & Ski Touring (pure mountain adventure)
QR Code (website)
www.peakhaven.eu
which languages ​​we speak (German, Czech, English and Russian)
Phone number, whatsapp sign and soc.media signs

```html
<!DOCTYPE html>
<html lang="de">
<head>
<meta charset="utf-8">
<title>Peakhaven Ski School – Private Lessons</title>
<link rel="stylesheet" href="https://fonts.googleapis.com/css2?family=Baloo+2:wght@700;800&family=Arimo:wght@400&display=swap">
<style>
  :root {
    --sky-top: #f2f8fc;
    --sky-mid: #bfe0f4;
    --sky-bottom: #5fb6e6;
    --heading: #ffffff;
    --heading-shadow: rgba(40, 120, 185, 0.45);
    --subline: #3c5d78;
    --accent: #9ad6f5;
    --footer-text: #ffffff;
  }
  html, body {
    margin: 0;
    padding: 0;
    overflow: hidden;
    background: #ffffff;
  }
  .flyer-back {
    position: relative;
    width: 851px;
    height: 1200px;
    overflow: hidden;
    background: linear-gradient(180deg, var(--sky-top) 0%, var(--sky-mid) 45%, var(--sky-bottom) 100%);
    font-family: "Arimo", Arial, sans-serif;
  }
  .offer-list {
    position: absolute;
    top: 92px;
    left: 0;
    width: 100%;
    text-align: center;
  }
  .offer {
    margin: 0;
  }
  .offer + .offer { margin-top: 13px; }
  .offer-group + .offer-group { margin-top: 50px; }
  .offer-title {
    margin: 0;
    font-family: "Baloo 2", "Arial Rounded MT Bold", sans-serif;
    font-weight: 800;
    font-size: 48px;
    line-height: 48px;
    letter-spacing: 0.5px;
    text-transform: uppercase;
    color: var(--heading);
    text-shadow: 0 1px 4px var(--heading-shadow);
  }
  .offer-note {
    margin: 4px 0 0;
    font-size: 27px;
    line-height: 32px;
    color: var(--subline);
  }
  .phone {
    position: absolute;
    top: 852px;
    left: 0;
    width: 100%;
    margin: 0;
    text-align: center;
    font-family: "Baloo 2", "Arial Rounded MT Bold", sans-serif;
    font-weight: 700;
    font-size: 92px;
    line-height: 100px;
    letter-spacing: 3px;
    color: var(--accent);
  }
  .contact-row {
    position: absolute;
    top: 990px;
    left: 257px;
    right: 90px;
    display: flex;
    align-items: center;
    gap: 40px;
  }
  .website {
    font-size: 34px;
    color: var(--accent);
  }
  .social {
    display: flex;
    align-items: center;
    gap: 10px;
    font-size: 30px;
    color: var(--footer-text);
  }
  .social-dot {
    width: 30px;
    height: 30px;
    border-radius: 50%;
    background: var(--footer-text);
  }
  .languages {
    position: absolute;
    top: 1072px;
    left: 0;
    width: 100%;
    margin: 0;
    text-align: center;
    font-size: 24px;
    color: var(--footer-text);
  }
</style>
</head>
<body>
  <main class="flyer-back">
    <section class="offer-list">
      <div class="offer-group">
        <div class="offer">
          <h2 class="offer-title">Privatunterricht</h2>
          <p class="offer-note">(Je besser du fährst, umso mehr Spaß hast du)</p>
        </div>
        <div class="offer">
          <h2 class="offer-title">Private Lessons</h2>
          <p class="offer-note">(the better you ride the more you enjoy)</p>
        </div>
      </div>
      <div class="offer-group">
        <div class="offer">
          <h2 class="offer-title">Für Familien &amp; Freunde</h2>
          <p class="offer-note">(endlich gemeinsam Urlaub machen)</p>
        </div>
        <div class="offer">
          <h2 class="offer-title">Families &amp; Friends</h2>
          <p class="offer-note">(go on holidays together)</p>
        </div>
      </div>
      <div class="offer-group">
        <div class="offer">
          <h2 class="offer-title">Freeride &amp; Skitouren</h2>
          <p class="offer-note">(ein unvergessliches Bergerlebnis)</p>
        </div>
        <div class="offer">
          <h2 class="offer-title">Freeride &amp; Ski Touring</h2>
          <p class="offer-note">(pure mountain adventure)</p>
        </div>
      </div>
    </section>

    <p class="phone">09876 543 210</p>

    <div class="contact-row">
      <span class="website">www.peakhaven.eu</span>
      <span class="social"><span class="social-dot"></span>peakhaven</span>
    </div>

    <p class="languages">We speak German, Czech, English and Russian</p>
  </main>
</body>
</html>
```